Bold Plum

I am starting a sharpening service for knives, scissors, and garden tools. It's a sole proprietorship, so it's a small business. The business name is "Bolt Plum." A one or two-page website is fine. Ember Guild has created a logo for me. There should be pictures of the things I sharpen. There will also be a price list for sharpened items. My address is: 18392 Calloway Lane, Stevenson Ranch, CA 91307. Phone number is 661-555-0172

```html
<!DOCTYPE html>
<html lang="en">
<head>
<meta charset="utf-8">
<title>Bolt Plum — Professional Sharpening</title>
<link href="https://fonts.googleapis.com/css2?family=Inter:wght@400;500;600;700&display=swap" rel="stylesheet">
<style>
:root{
  --gold:#d4a24c;
  --ink:#141414;
  --ink-2:#1c1c1c;
  --text:#1a1a1a;
  --muted:#6f6f6f;
  --line:#ececec;
  --soft:#f8f8f8;
  --white:#ffffff;
}
*{box-sizing:border-box;margin:0;padding:0}
html,body{width:1200px;height:2989px;overflow:hidden}
body{position:relative;background:var(--white);font-family:'Inter',sans-serif;color:var(--text)}
.abs{position:absolute}
.eyebrow{font-size:8px;letter-spacing:3px;font-weight:600;color:var(--gold);text-transform:uppercase}
.center{left:0;width:1200px;text-align:center}
.sec-title{font-size:26px;font-weight:700;letter-spacing:-0.3px}
.sec-sub{font-size:11.5px;color:var(--muted);line-height:19px}

/* nav */
.nav{left:120px;top:9px;width:960px;height:39px;border-radius:20px;background:rgba(120,120,120,.75);border:1px solid rgba(255,255,255,.35);display:flex;align-items:center;padding:0 16px 0 22px;z-index:5}
.brand{display:flex;align-items:center;gap:6px;color:var(--white);font-size:12px;font-weight:700;white-space:nowrap}
.brand-mark{width:12px;height:12px;background:currentColor}
.nav-links{position:absolute;left:0;width:100%;text-align:center;font-size:10px;color:var(--white);pointer-events:none}
.nav-links span{margin:0 9px}
.nav-cta{margin-left:auto;background:var(--gold);color:var(--ink);font-size:9px;font-weight:600;padding:7px 13px;border-radius:14px}

/* hero */
.hero{left:0;top:0;width:1200px;height:637px;clip-path:polygon(0 0,100% 0,100% 100%,0 598px);
  background:radial-gradient(ellipse 110px 340px at 615px 330px,#3a3a3a 0%,#1e1e1e 45%,transparent 100%),linear-gradient(180deg,#222 0%,#141414 60%,#0f0f0f 100%)}
.hero-eyebrow{left:112px;top:207px}
.hero-title{left:112px;top:226px;width:400px;font-size:37px;line-height:44px;font-weight:700;color:var(--white);letter-spacing:-0.5px}
.hero-title em{font-style:normal;color:var(--gold)}
.hero-copy{left:112px;top:322px;width:360px;font-size:12px;line-height:20px;color:#e4e4e4}
.btn{position:absolute;top:403px;height:33px;border-radius:3px;font-size:10px;font-weight:600;display:flex;align-items:center;justify-content:center}
.btn-gold{left:112px;width:100px;background:var(--gold);color:var(--ink)}
.btn-white{left:221px;width:137px;background:var(--white);color:var(--ink)}

/* services */
.card{background:var(--white);border:1px solid var(--line);border-radius:6px;overflow:hidden;box-shadow:0 1px 3px rgba(0,0,0,.04)}
.svc{top:854px;width:221px;height:251px}
.svc-img{height:133px}
.svc h3{font-size:14px;font-weight:600;margin:17px 16px 8px}
.svc p{font-size:9.5px;line-height:15.5px;color:var(--muted);margin:0 16px}

/* how */
.how-band{left:0;top:1123px;width:1200px;height:429px;background:var(--soft);clip-path:polygon(0 37px,100% 0,100% 391px,0 100%)}
.step-line{left:356px;top:1385px;width:486px;height:1px;background:#dcdcdc}
.step{width:190px;text-align:center}
.step-num{width:48px;height:48px;border-radius:50%;background:var(--ink);color:var(--white);font-size:15px;font-weight:600;display:flex;align-items:center;justify-content:center;margin:0 auto}
.step h4{font-size:14px;font-weight:600;margin-top:13px}
.step p{font-size:9.5px;line-height:15.5px;color:var(--muted);margin-top:6px}

/* pricing */
.price{top:1749px;width:221px;height:280px}
.price-head{height:42px;background:var(--ink);color:var(--white);display:flex;align-items:center;gap:9px;padding:0 16px;font-size:12px;font-weight:600}
.price-list{list-style:none;padding-top:3px}
.price-list li{height:32.5px;margin:0 16px;display:flex;align-items:center;justify-content:space-between;font-size:9.5px;color:#555;border-bottom:1px solid var(--line)}
.price-list li:last-child{border-bottom:none}
.price-list b{color:var(--text);font-weight:700}

/* why */
.why-band{left:0;top:2050px;width:1200px;height:465px;background:var(--ink);clip-path:polygon(0 38px,100% 0,100% 100%,0 424px)}
.why{top:2286px;width:162px;height:170px;background:var(--ink-2);border:1px solid #262626;border-radius:6px;text-align:center;color:var(--white)}
.why-icon{width:36px;height:36px;border-radius:6px;background:#3a3224;margin:22px auto 0;display:flex;align-items:center;justify-content:center}
.why h4{font-size:11px;font-weight:600;margin-top:14px}
.why p{font-size:9px;line-height:15px;color:#a8a8a8;margin:6px 12px 0}

/* contact */
.contact-item{left:249px;display:flex;gap:11px}
.c-icon{width:29px;height:29px;border-radius:6px;background:var(--ink);display:flex;align-items:center;justify-content:center;flex:none}
.c-text{font-size:9.5px;line-height:17px;color:var(--muted)}
.c-text strong{display:block;color:var(--text);font-size:10px;font-weight:600}
.map{left:620px;top:2602px;width:330px;height:248px;border-radius:4px;background:linear-gradient(135deg,#eef0f2 0%,#e4e8ec 55%,#dfe9df 100%)}

/* footer */
.footer-line{left:0;top:2917px;width:1200px;height:1px;background:var(--line)}
.foot-brand{left:251px;top:2949px;color:var(--ink)}
.foot-copy{left:334px;top:2951px;font-size:9px;color:var(--muted)}
.foot-links{right:250px;top:2951px;font-size:9px;color:var(--muted)}
.foot-links span{margin-left:20px}
</style>
</head>
<body>

<!-- HERO -->
<div class="abs hero" role="img" aria-label="Photo of a long dark knife blade held upright against a black background"></div>
<nav class="abs nav">
  <div class="brand"><span class="brand-mark"></span>Bolt Plum</div>
  <div class="nav-links"><span>Services</span><span>Pricing</span><span>Why Us</span><span>Contact</span></div>
  <div class="nav-cta">Call Now</div>
</nav>
<div class="abs eyebrow hero-eyebrow">Professional Sharpening Service</div>
<h1 class="abs hero-title">Dull Blades? <em>Bolt<br>Plum.</em></h1>
<p class="abs hero-copy">Expert sharpening for knives, scissors, and garden tools. Restore factory-edge precision to your favorite blades — right here in Stevenson Ranch, CA.</p>
<div class="btn btn-gold">View Pricing</div>
<div class="btn btn-white">Call (661) 555-0172</div>

<!-- SERVICES -->
<div class="abs eyebrow center" style="top:723px">What We Sharpen</div>
<h2 class="abs sec-title center" style="top:740px">Our Services</h2>
<p class="abs sec-sub center" style="top:779px">From kitchen knives to garden loppers, we bring back the edge your<br>tools were meant to have.</p>

<div class="abs card svc" style="left:249px">
  <div class="svc-img" role="img" aria-label="Photo of kitchen knives and a wooden knife block" style="background:linear-gradient(160deg,#6a6a6a,#2c2c2c 60%,#8a5a3a)"></div>
  <h3>Knives</h3>
  <p>Kitchen knives, chef's knives, cleavers, paring knives, pocket knives, hunting knives — we sharpen them all to a razor-sharp edge.</p>
</div>
<div class="abs card svc" style="left:490px">
  <div class="svc-img" role="img" aria-label="Photo of a pair of scissors on a dark teal surface" style="background:linear-gradient(160deg,#1d3234,#16292b 60%,#1c3a3e)"></div>
  <h3>Scissors</h3>
  <p>Household scissors, kitchen shears, hair &amp; grooming shears, and pinking shears. Precision-sharpened for clean, effortless cuts.</p>
</div>
<div class="abs card svc" style="left:729px">
  <div class="svc-img" role="img" aria-label="Photo of an axe resting on a tree stump" style="background:linear-gradient(160deg,#4a3f33,#7a6a58 50%,#3b3127)"></div>
  <h3>Garden Tools</h3>
  <p>Pruning shears, hedge shears, loppers, lawn mower blades, axes, and shovels. Keep your yard tools cutting like new.</p>
</div>

<!-- HOW IT WORKS -->
<div class="abs how-band"></div>
<div class="abs eyebrow center" style="top:1251px">Simple Process</div>
<h2 class="abs sec-title center" style="top:1268px">How It Works</h2>
<p class="abs sec-sub center" style="top:1306px">Getting your blades sharpened couldn't be easier.</p>
<div class="abs step-line"></div>
<div class="abs step" style="left:261px;top:1361px"><div class="step-num">1</div><h4>Bring Your Blades</h4><p>Drop off your dull knives, scissors, or tools at our Stevenson Ranch location.</p></div>
<div class="abs step" style="left:505px;top:1361px"><div class="step-num">2</div><h4>We Sharpen</h4><p>Using professional-grade equipment, we restore a precise, long-lasting edge to every blade.</p></div>
<div class="abs step" style="left:747px;top:1361px"><div class="step-num">3</div><h4>Pick Up &amp; Cut</h4><p>Collect your razor-sharp tools and enjoy effortless cutting again. That's it!</p></div>

<!-- PRICING -->
<div class="abs eyebrow center" style="top:1638px">Fair &amp; Transparent</div>
<h2 class="abs sec-title center" style="top:1654px">Pricing</h2>
<p class="abs sec-sub center" style="top:1693px">Quality sharpening at honest prices. No hidden fees, no surprises.</p>

<div class="abs card price" style="left:249px">
  <div class="price-head"><svg width="14" height="14" viewBox="0 0 14 14" fill="none" stroke="#d4a24c" stroke-width="1.2"><path d="M2 12 L11 3 L12 4 L5 12 Z"/></svg>Knives</div>
  <ul class="price-list">
    <li>Kitchen Knife (up to 6")<b>$8</b></li>
    <li>Kitchen Knife (7"–10")<b>$10</b></li>
    <li>Kitchen Knife (over 10")<b>$12</b></li>
    <li>Serrated Knife<b>$10</b></li>
    <li>Paring Knife<b>$6</b></li>
    <li>Cleaver<b>$12</b></li>
    <li>Pocket / Hunting Knife<b>$8</b></li>
  </ul>
</div>
<div class="abs card price" style="left:490px">
  <div class="price-head"><svg width="14" height="14" viewBox="0 0 14 14" fill="none" stroke="#d4a24c" stroke-width="1.2"><circle cx="3.5" cy="3.5" r="2"/><circle cx="3.5" cy="10.5" r="2"/><path d="M5 5 L12 12 M5 9 L12 2"/></svg>Scissors</div>
  <ul class="price-list">
    <li>Household Scissors<b>$8</b></li>
    <li>Kitchen Shears<b>$10</b></li>
    <li>Hair / Grooming Shears<b>$15</b></li>
    <li>Pinking Shears<b>$12</b></li>
  </ul>
</div>
<div class="abs card price" style="left:729px">
  <div class="price-head"><svg width="14" height="14" viewBox="0 0 14 14" fill="none" stroke="#d4a24c" stroke-width="1.2"><circle cx="7" cy="8" r="4.5"/><path d="M7 3.5 V1.5 M5.5 1.5 H8.5"/></svg>Garden Tools</div>
  <ul class="price-list">
    <li>Pruning Shears / Secateurs<b>$10</b></li>
    <li>Hedge Shears<b>$14</b></li>
    <li>Loppers<b>$14</b></li>
    <li>Lawn Mower Blade<b>$15</b></li>
    <li>Axe / Hatchet<b>$12</b></li>
    <li>Shovel / Spade Edge<b>$10</b></li>
  </ul>
</div>

<!-- WHY -->
<div class="abs why-band"></div>
<div class="abs eyebrow center" style="top:2174px">The Bolt Plum Difference</div>
<h2 class="abs sec-title center" style="top:2191px;color:var(--white)">Why Choose Us</h2>
<p class="abs sec-sub center" style="top:2230px;color:#d0d0d0">We're a local business that takes pride in every edge we restore.</p>

<div class="abs why" style="left:249px"><div class="why-icon"><svg width="16" height="16" viewBox="0 0 16 16" fill="none" stroke="#d4a24c" stroke-width="1.3"><circle cx="8" cy="8" r="6"/><path d="M5.5 8 L7.3 9.8 L11 6"/></svg></div><h4>Precision Results</h4><p>Professional-grade sharpening that restores factory-edge quality to every blade.</p></div>
<div class="abs why" style="left:429px"><div class="why-icon"><svg width="16" height="16" viewBox="0 0 16 16" fill="none" stroke="#d4a24c" stroke-width="1.3"><circle cx="8" cy="8" r="6"/><path d="M8 4.5 V8 L10.3 9.5"/></svg></div><h4>Fast Turnaround</h4><p>Most items sharpened and ready for pickup quickly, so you're never without your tools for long.</p></div>
<div class="abs why" style="left:609px"><div class="why-icon"><svg width="16" height="16" viewBox="0 0 16 16" fill="none" stroke="#d4a24c" stroke-width="1.3"><rect x="6" y="2" width="4" height="7" rx="2"/><path d="M4 8 A4 4 0 0 0 12 8 M8 12 V14"/></svg></div><h4>Local &amp; Personal</h4><p>A small business built on trust. You'll work directly with the owner every time.</p></div>
<div class="abs why" style="left:789px"><div class="why-icon"><svg width="16" height="16" viewBox="0 0 16 16" fill="none" stroke="#d4a24c" stroke-width="1.3"><path d="M8 2 V14 M10.5 4.5 H6.8 A1.8 1.8 0 0 0 6.8 8 H9.2 A1.8 1.8 0 0 1 9.2 11.5 H5.5"/></svg></div><h4>Fair Pricing</h4><p>Honest, upfront prices with no hidden costs. Quality sharpening shouldn't break the bank.</p></div>

<!-- CONTACT -->
<div class="abs eyebrow" style="left:249px;top:2601px">Get In Touch</div>
<h2 class="abs sec-title" style="left:249px;top:2617px">Ready to Bolt Plum?</h2>
<p class="abs sec-sub" style="left:249px;top:2659px;width:320px">Bring your dull knives, scissors, and garden tools to us. We're conveniently located in Stevenson Ranch, California.</p>

<div class="abs contact-item" style="top:2716px"><div class="c-icon"><svg width="13" height="13" viewBox="0 0 14 14" fill="none" stroke="#d4a24c" stroke-width="1.2"><path d="M7 13 C7 13 2.5 8.5 2.5 5.5 A4.5 4.5 0 0 1 11.5 5.5 C11.5 8.5 7 13 7 13 Z"/><circle cx="7" cy="5.5" r="1.5"/></svg></div><div class="c-text"><strong>Address</strong>18392 Calloway Lane<br>Stevenson Ranch, CA 91307</div></div>
<div class="abs contact-item" style="top:2778px"><div class="c-icon"><svg width="13" height="13" viewBox="0 0 14 14" fill="none" stroke="#d4a24c" stroke-width="1.2"><path d="M3 1.5 L5 1.5 L6 4.5 L4.5 5.5 A7 7 0 0 0 8.5 9.5 L9.5 8 L12.5 9 L12.5 11 A1.5 1.5 0 0 1 11 12.5 A10 10 0 0 1 1.5 3 A1.5 1.5 0 0 1 3 1.5 Z"/></svg></div><div class="c-text"><strong>Phone</strong><span style="color:var(--gold)">(661) 555-0172</span></div></div>
<div class="abs contact-item" style="top:2823px"><div class="c-icon"><svg width="13" height="13" viewBox="0 0 14 14" fill="none" stroke="#d4a24c" stroke-width="1.2"><circle cx="7" cy="7" r="5.5"/><path d="M7 4 V7 L9 8.3"/></svg></div><div class="c-text"><strong>Hours</strong>By appointment — call or text to schedule</div></div>

<div class="abs map" role="img" aria-label="Street map showing the shop location in Stevenson Ranch"></div>

<!-- FOOTER -->
<div class="abs footer-line"></div>
<div class="abs brand foot-brand" style="font-size:11px"><span class="brand-mark" style="width:10px;height:10px"></span>Bolt Plum</div>
<div class="abs foot-copy">© 2026 Bolt Plum. All rights reserved.</div>
<div class="abs foot-links"><span>Services</span><span>Pricing</span><span>Contact</span></div>

</body>
</html>
```